Morvela Aesthetic Doctor

I require an elegant, luxurious looking business card for my aesthetic business. I am a doctor and that will set me aside from competitors. I am planning to provide home and spa based treatments to clients with high expectations. I have attached my logo.

```html
<!DOCTYPE html>
<html lang="en">
<head>
<meta charset="utf-8">
<title>Morvela Aesthetic Doctor – Business Card</title>
<link rel="stylesheet" href="https://fonts.googleapis.com/css2?family=Lato:wght@300;400;700&display=swap">
<style>
  :root {
    --paper: #f5f5f5;
    --brand-blue: #0f6fc6;
    --ring-blue: #8fd0ee;
    --arc-grey: #8a8a8a;
    --ink: #2b2b2b;
    --logo-grey: #9a9a9a;
    --white: #ffffff;
    --mist: #d6d6d6;
  }
  * { margin: 0; padding: 0; box-sizing: border-box; }
  html, body { width: 1200px; height: 720px; overflow: hidden; background: var(--paper); }
  .card {
    position: relative; width: 1200px; height: 720px; overflow: hidden;
    background: var(--paper); font-family: "Lato", sans-serif; color: var(--ink);
  }
  .card__shapes { position: absolute; inset: 0; }
  .card__mist {
    position: absolute; left: 0; bottom: 0; width: 230px; height: 150px;
    background: radial-gradient(ellipse at 0% 80%, var(--mist) 0%, rgba(214,214,214,0.4) 45%, rgba(245,245,245,0) 75%);
  }
  .brand { position: absolute; left: 34px; top: 306px; }
  .brand__mark { display: flex; align-items: center; gap: 22px; }
  .brand__dot {
    width: 104px; height: 104px; border-radius: 50%;
    border: 3px solid var(--logo-grey);
  }
  .brand__name { color: var(--logo-grey); font-weight: 300; line-height: 1; }
  .brand__name-main { display: block; font-size: 54px; letter-spacing: 2px; }
  .brand__name-sub { display: block; font-size: 21px; letter-spacing: 2px; margin-top: 8px; }
  .brand__tagline { margin-top: 12px; font-size: 25px; font-weight: 400; color: var(--ink); }

  .details { position: absolute; right: 46px; top: 82px; text-align: right; color: var(--white); }
  .details__name { font-size: 45px; font-weight: 700; line-height: 1; }
  .details__post { font-size: 26.5px; font-weight: 400; }
  .details__diploma { font-size: 26.5px; font-weight: 400; margin-top: 2px; }

  .contact { list-style: none; margin-top: 30px; }
  .contact__item {
    display: flex; justify-content: flex-end; align-items: center; gap: 14px;
    font-size: 30px; height: 53px;
  }
  .contact__icon { width: 22px; height: 22px; flex: none; }

  .services { list-style: none; margin-top: 24px; }
  .services__item {
    display: flex; justify-content: flex-end; align-items: center; gap: 24px;
    font-size: 26.5px; height: 40px;
  }
  .services__item::after {
    content: ""; width: 8px; height: 8px; border-radius: 50%; background: var(--white);
    margin-right: 4px;
  }

  .social { position: absolute; right: 46px; top: 638px; display: flex; gap: 14px; }
  .social__spot { width: 26px; height: 26px; border-radius: 50%; background: var(--white); }
</style>
</head>
<body>
<main class="card">
  <svg class="card__shapes" width="1200" height="720" viewBox="0 0 1200 720" aria-hidden="true">
    <path d="M640 40 A535 535 0 0 0 592 660" fill="none" stroke="var(--arc-grey)" stroke-width="3"/>
    <circle cx="1040" cy="384" r="510" fill="var(--ring-blue)"/>
    <circle cx="1040" cy="384" r="491" fill="var(--brand-blue)"/>
  </svg>

  <div class="card__mist" role="img" aria-label="Soft grey flowing hair-like decorative swirl"></div>

  <section class="brand">
    <div class="brand__mark">
      <span class="brand__dot"></span>
      <span class="brand__name">
        <span class="brand__name-main">MORVELA</span>
        <span class="brand__name-sub">AESTHETIC DOCTOR</span>
      </span>
    </div>
    <p class="brand__tagline">Home and Spa Based Treatments</p>
  </section>

  <section class="details">
    <h1 class="details__name">Dr Mira Holt <span class="details__post">MRCPCH MD</span></h1>
    <p class="details__diploma">Australasian Diploma of Aesthetic Medicine</p>

    <ul class="contact">
      <li class="contact__item">0800 555 014
        <svg class="contact__icon" viewBox="0 0 24 24"><path fill="#fff" d="M6.6 10.8a15.1 15.1 0 0 0 6.6 6.6l2.2-2.2a1 1 0 0 1 1-.25 11.4 11.4 0 0 0 3.6.57 1 1 0 0 1 1 1V20a1 1 0 0 1-1 1A17 17 0 0 1 3 4a1 1 0 0 1 1-1h3.5a1 1 0 0 1 1 1c0 1.25.2 2.45.57 3.57a1 1 0 0 1-.25 1z"/></svg>
      </li>
      <li class="contact__item">mira@morvela.co.nz
        <svg class="contact__icon" viewBox="0 0 24 24"><rect x="3" y="7" width="18" height="12" rx="1.5" fill="#fff"/><path d="M3.5 8l8.5 6 8.5-6" fill="none" stroke="var(--brand-blue)" stroke-width="1.6"/></svg>
      </li>
      <li class="contact__item">www.morvela.co.nz
        <svg class="contact__icon" viewBox="0 0 24 24" fill="none" stroke="#fff" stroke-width="1.8"><circle cx="12" cy="12" r="9"/><ellipse cx="12" cy="12" rx="4" ry="9"/><path d="M3 12h18M5 7h14M5 17h14"/></svg>
      </li>
    </ul>

    <ul class="services">
      <li class="services__item">Dermal injectables</li>
      <li class="services__item">Plasma facials</li>
      <li class="services__item">Microneedling</li>
      <li class="services__item">Skin boosters</li>
      <li class="services__item">Excessive sweating</li>
    </ul>
  </section>

  <div class="social" aria-label="Social media">
    <span class="social__spot"></span>
    <span class="social__spot"></span>
  </div>
</main>
</body>
</html>
```